pipequell new business sales flyer

this is a flyer to tell people what pipequell does and what is great about the service we offer.

please see attached doc for brief, and add the contact details below.

12/18-26 Wexbury Rd, Brenton Vale VIC 3990
03 9461 2078
0428 716 304
bookings@pipequell.com.au
www.pipequell.com.au

Target Market(s)

home builder companies

Industry/Entity Type

residential home building construction

Colors
0054AA
0677BA
7BADD7
CADEEF
E8F1F8
0094D4
00A9DD
6FCCEA
C7EBF8
E9F6FB
FFC000
F8CF3A
FAE287
FDF2CF
FEFAEE

Requirements
Must have
• logo/images/

```html
<!DOCTYPE html>
<html lang="en">
<head>
<meta charset="utf-8">
<title>pipequell – Builder Drain Inspections</title>
<link href="https://fonts.googleapis.com/css2?family=Montserrat:wght@300;400;500;600;700;800&display=swap" rel="stylesheet">
<style>
  :root {
    --navy: #243a8c;
    --cyan: #00b1de;
    --ink: #1f2a55;
    --white: #ffffff;
  }
  * { margin: 0; padding: 0; box-sizing: border-box; }
  html, body { width: 893px; height: 1200px; overflow: hidden; background: var(--white); }
  body { font-family: "Montserrat", sans-serif; color: var(--ink); }
  .flyer { position: relative; width: 893px; height: 1200px; overflow: hidden; background: var(--white); }
  .abs { position: absolute; }

  .corner-shape { left: 0; top: 0; }

  .brand { left: 46px; top: 62px; display: flex; align-items: center; gap: 12px; }
  .brand-name { font-size: 64px; font-weight: 700; color: var(--navy); line-height: 1; }
  .brand-dot { width: 22px; height: 22px; border-radius: 50%; background: var(--cyan); margin-top: 14px; }
  .brand-tagline { left: 48px; top: 142px; font-size: 14px; font-weight: 600; color: var(--cyan); letter-spacing: 1.2px; }

  .hero-band { left: 0; top: 211px; width: 450px; height: 433px;
    background: linear-gradient(160deg, #2b3f96 0%, #243a8c 55%, #1d2f78 100%); }

  .headline { left: 46px; top: 252px; color: var(--white); font-weight: 800; text-transform: uppercase; }
  .headline .lead { font-size: 29.5px; line-height: 35px; }
  .headline .accent { font-size: 58px; line-height: 53px; color: var(--cyan); margin-top: 5px; letter-spacing: -0.5px; }

  .hero-copy { left: 46px; top: 504px; color: var(--white); font-size: 23px; line-height: 28px; }
  .hero-copy strong { font-weight: 700; display: block; }
  .hero-copy span { font-weight: 300; display: block; letter-spacing: 0.3px; }

  .drop-visual { left: 0; top: 0; }

  .problem-photo { width: 126px; height: 126px; border-radius: 50%; top: 658px;
    border: 3px solid var(--white); box-shadow: 0 0 0 2px var(--navy); }
  .problem-photo.brick { left: 46px; background: linear-gradient(135deg, #a65a48, #7e3d31); }
  .problem-photo.pipe { left: 189px; background: radial-gradient(circle at 50% 45%, #2a2116 0%, #6c5a3c 45%, #d9cfb4 80%); }
  .problem-photo.wall { left: 331px; background: linear-gradient(135deg, #f2f2f0, #dcdcd8); }

  .section-title { font-size: 21px; font-weight: 800; color: var(--navy); text-transform: uppercase; line-height: 32px; }
  .rule { height: 5px; }
  .rule::before { content: ""; position: absolute; left: 0; top: 0; width: 64px; height: 5px; background: var(--cyan); }
  .rule::after { content: ""; position: absolute; left: 64px; top: 2px; right: 0; height: 1px; background: var(--cyan); }

  .body-copy { font-size: 11.3px; line-height: 13.6px; color: var(--ink); }
  .body-copy p + p { margin-top: 11px; }
  .body-copy .justified { text-align: justify; }

  .service { display: flex; align-items: center; gap: 10px; top: 1042px; }
  .service-icon { width: 56px; height: 56px; border-radius: 50%; border: 3px solid var(--navy);
    display: flex; align-items: center; justify-content: center; background: var(--white); }
  .service-label { font-size: 14.5px; font-weight: 700; line-height: 17px; color: var(--navy); }
  .service-label em { font-style: normal; color: var(--cyan); display: block; }

  .cta-line { left: 471px; top: 1018px; font-size: 22px; font-weight: 400; color: var(--ink); }
  .phone-bar { left: 471px; top: 1060px; width: 379px; height: 39px; display: flex; background: var(--cyan); }
  .phone-bar .phone-icon { width: 36px; height: 39px; background: var(--navy); display: flex; align-items: center; justify-content: center; }
  .phone-bar .number { color: var(--white); font-size: 20.5px; font-weight: 700; display: flex; align-items: center; padding: 0 12px; white-space: nowrap; }
  .phone-bar .divider { width: 1px; margin: 6px 0; background: var(--white); }

  .footer { left: 0; top: 1122px; width: 893px; height: 65px; background: var(--navy);
    display: flex; align-items: center; padding-left: 44px; color: var(--white); font-size: 13.6px; font-weight: 600; white-space: nowrap; }
  .footer .sep { width: 1px; height: 45px; background: var(--cyan); margin: 0 10px; }
</style>
</head>
<body>
<div class="flyer">

  <svg class="abs corner-shape" width="893" height="1200" viewBox="0 0 893 1200" aria-hidden="true">
    <polygon points="782,0 893,0 893,145" fill="var(--navy)"/>
  </svg>

  <div class="abs brand">
    <div class="brand-name">pipequell</div>
    <div class="brand-dot"></div>
  </div>
  <div class="abs brand-tagline">INSPECTIONS · REPAIRS · REPORTS</div>

  <div class="abs hero-band" role="img" aria-label="Navy-tinted photo of a drainage worker in overalls"></div>

  <svg class="abs drop-visual" width="893" height="1200" viewBox="0 0 893 1200">
    <defs>
      <linearGradient id="photoTone" x1="0" y1="0" x2="0" y2="1">
        <stop offset="0" stop-color="#ffffff"/>
        <stop offset="0.3" stop-color="#eef0f4"/>
        <stop offset="0.65" stop-color="#c3c7d1"/>
        <stop offset="1" stop-color="#3d4f9a"/>
      </linearGradient>
    </defs>
    <path d="M690,-60 L874,349 A246 246 0 1 1 444,315 Z" fill="url(#photoTone)" stroke="var(--cyan)" stroke-width="24"
      role="img" aria-label="Photo of a plumber crouching on site, feeding a drain camera cable into a pipe"/>
  </svg>

  <div class="abs headline">
    <div class="lead">We have the capacity<br>to take on the</div>
    <div class="accent">Largest<br>Volume<br>Builders!</div>
  </div>

  <div class="abs hero-copy">
    <strong>With over 50,000 jobs<br>under our belt,</strong>
    <span>we know a thing or two<br>about drainage problems.</span>
  </div>

  <div class="abs problem-photo brick" role="img" aria-label="Cracked brick wall"></div>
  <div class="abs problem-photo pipe" role="img" aria-label="Inside of a blocked drain pipe"></div>
  <div class="abs problem-photo wall" role="img" aria-label="Crack in a rendered wall"></div>

  <h2 class="abs section-title" style="left:44px; top:796px;">What we do?</h2>
  <div class="abs rule" style="left:44px; top:829px; width:248px;"></div>
  <div class="abs body-copy" style="left:44px; top:850px; width:380px;">
    <p>Long-term sewer and stormwater damage on new home builds is hitting builders where it hurts, it severely impacts both your reputation and your bank balance.<br>We've got the solution!</p>
    <p class="justified">Our fixed-price Drainage Inspection Package catches issues before homeowners move in. Our Post-Slab &amp;Pre Settlement Drain Inspection on every build, sees repairs fixed on the spot, all included in the one low fixed-price. You'll receive a comprehensive report &amp; video footage for each inspection. We pride ourselves on our reputation, customer service is at the forefront of everything we do.</p>
  </div>

  <div class="abs service" style="left:44px;">
    <div class="service-icon">
      <svg width="32" height="32" viewBox="0 0 32 32" aria-hidden="true">
        <circle cx="13" cy="17" r="8" fill="none" stroke="var(--cyan)" stroke-width="5" stroke-dasharray="4 2.3"/>
        <circle cx="13" cy="17" r="3" fill="var(--cyan)"/>
        <path d="M23 5 v22" stroke="var(--navy)" stroke-width="4" stroke-linecap="round"/>
        <path d="M19 4 q4 5 8 0" fill="none" stroke="var(--navy)" stroke-width="3"/>
      </svg>
    </div>
    <div class="service-label">CC TV DRAIN<br>INSPECTION<em>+ REPAIRS</em></div>
  </div>

  <div class="abs service" style="left:253px;">
    <div class="service-icon">
      <svg width="30" height="32" viewBox="0 0 30 32" aria-hidden="true">
        <rect x="9" y="7" width="15" height="20" fill="none" stroke="var(--cyan)" stroke-width="2.5"/>
        <rect x="5" y="3" width="15" height="20" fill="var(--white)" stroke="var(--navy)" stroke-width="2.5"/>
        <path d="M8 9 h9 M8 13 h9 M8 17 h9" stroke="var(--navy)" stroke-width="2"/>
      </svg>
    </div>
    <div class="service-label">CC TV DRAIN<br>INSPECTION<em>+ REPORTINGS</em></div>
  </div>

  <h2 class="abs section-title" style="left:471px; top:796px;">What is slab heave<br>costing your business?</h2>
  <div class="abs rule" style="left:471px; top:855px; width:238px;"></div>
  <div class="abs body-copy" style="left:471px; top:874px; width:380px;">
    <p>The SBC (State Building Council) put out a report regarding the growing concern of slab heave in new homes.</p>
    <p>One of their recommendations to eliminate the problem is to conduct an independent inspection (rather than self-certification) of installed stormwater drainage systems. This should be an extension of mandatory inspections for building structures. Pipequell are the only specialized drainage inspectors to offer a cost-effective independent solution to inspect drains on each site. We are saving our home builder clients a lot of money.</p>
  </div>

  <div class="abs cta-line">Talk to us today about how.</div>
  <div class="abs phone-bar">
    <div class="phone-icon">
      <svg width="20" height="20" viewBox="0 0 24 24" aria-hidden="true">
        <path d="M6.6 10.8c1.4 2.8 3.8 5.1 6.6 6.6l2.2-2.2c.3-.3.7-.4 1-.2 1.1.4 2.3.6 3.6.6.6 0 1 .4 1 1V20c0 .6-.4 1-1 1C10.6 21 3 13.4 3 4c0-.6.4-1 1-1h3.5c.6 0 1 .4 1 1 0 1.3.2 2.5.6 3.6.1.3 0 .7-.2 1z" fill="var(--cyan)"/>
      </svg>
    </div>
    <div class="number">03 9461 2078</div>
    <div class="divider"></div>
    <div class="number">0428 716 304</div>
  </div>

  <div class="abs footer">
    <span>bookings@pipequell.com.au</span>
    <span class="sep"></span>
    <span>www.pipequell.com.au</span>
    <span class="sep"></span>
    <span>12/18-26 Wexbury Rd, Brenton Vale VIC 3990</span>
  </div>

</div>
</body>
</html>
```